small business website design

***Update: need the design to be coded into a wordpress or similar format***
Need a website for a small business with big plans. No online ordering etc but business description and contact details pages, a page showing products we use and page for customers or suppliers to register with us. Also want links to quillane. We have a logo existing but also open to any improvements on the design. We have an existing website we created and looks very DIY but you can get some info from it to help create your design for us.
Updates
Hi Everyone, we didn't make it clear at the beginning but we would like the final design to be in a coded format and ready to upload to a URL. I have to apologise and admit to my lack of knowledge of the design process.
Target Market(s)
Oil / gas and industrial plant managers.
Industry/Entity Type
Small Business
Look and feel
Each slider illustrates characteristics of the customer's brand and the style your logo design should communicate.

```html
<!DOCTYPE html>
<html lang="en">
<head>
<meta charset="utf-8">
<title>Meridian Tank Metering</title>
<link rel="stylesheet" href="https://fonts.googleapis.com/css2?family=Source+Sans+3:wght@400;600&display=swap">
<style>
:root{
  --page:#d8d8d8;
  --sheet:#ececec;
  --blue:#2a93c4;
  --blue-deep:#1f7fb0;
  --ink:#333;
  --muted:#666;
  --rule:#cfcfcf;
  --footer:#2f2f2f;
  --footer-base:#222;
  --accent:#e8541c;
  --heading:"Source Sans 3",sans-serif;
  --body:Arial,Helvetica,sans-serif;
}
*{box-sizing:border-box;margin:0;padding:0}
html,body{width:1182px;height:1200px;overflow:hidden;background:var(--page)}
.frame{position:absolute;left:0;top:0;width:1200px;height:1217px;transform:scale(.985);transform-origin:0 0;font-family:var(--body);color:var(--ink)}
.sheet{position:absolute;left:102px;top:4px;width:996px;height:1088px;background:var(--sheet)}
.topline{position:absolute;left:0;top:0;width:1200px;height:4px;background:#444}
.brand{position:absolute;left:115px;top:36px;display:flex;align-items:center;gap:12px}
.brand-dot{width:54px;height:54px;border-radius:50%;background:var(--blue)}
.brand-name{font-family:var(--heading);font-weight:600;font-size:30px;color:var(--blue);line-height:1}
.brand-name small{display:block;font-size:13px;color:#333;font-weight:400;margin-top:4px}
.social{position:absolute;left:896px;top:49px;display:flex;gap:6px}
.social span{width:33px;height:33px;border-radius:50%;border:1px solid #bbb;background:#f6f6f6}
.wave{position:absolute;left:0;top:90px}
.hero-photo{position:absolute;left:120px;top:138px;width:962px;height:398px;background:linear-gradient(180deg,#b9d3e8 0%,#8aa0ad 38%,#6f7a6c 62%,#8d8a7c 100%)}
.services{position:absolute;left:760px;top:120px;width:312px;height:406px;background:rgba(248,248,248,.9);border-radius:3px;padding:36px 0 0 10px}
.services h2{font-family:var(--heading);font-weight:400;font-size:31px;color:#222;line-height:1;white-space:nowrap}
.services h2 em{font-style:normal;color:var(--blue)}
.services ul{list-style:none;margin-top:18px}
.services li{font-family:var(--heading);font-size:15px;letter-spacing:.3px;color:#333;height:30px;padding-left:19px;position:relative}
.services li::before{content:"";position:absolute;left:7px;top:6px;border-left:4px solid #555;border-top:3px solid transparent;border-bottom:3px solid transparent}
h3{font-family:var(--heading);font-weight:400;color:var(--blue);line-height:1}
.about h3{position:absolute;left:123px;top:578px;font-size:31px}
.can{position:absolute;left:125px;top:639px;width:106px;height:106px;border-radius:10px;background:linear-gradient(90deg,#8c8c8c,#e6e6e6 45%,#9a9a9a)}
.about p{position:absolute;left:250px;top:633px;width:505px;font-size:12.8px;line-height:20px;color:#333}
.divider{position:absolute;left:768px;top:582px;width:1px;height:465px;background:var(--rule)}
.support h3{position:absolute;left:796px;top:578px;font-size:31px}
.support p{position:absolute;left:796px;top:631px;width:290px;font-size:12.5px;line-height:20px}
.news h3,.testimonials h3,.tweets h3{position:absolute;font-size:24px}
.news h3{left:125px;top:797px}
.news h4{position:absolute;left:129px;top:844px;font-family:var(--heading);font-weight:600;font-size:18px;color:#333}
.news .date{position:absolute;left:129px;top:870px;font-family:var(--heading);font-size:13px;color:var(--muted)}
.news p{position:absolute;left:129px;top:902px;width:276px;font-family:var(--heading);font-size:13px;line-height:23px;color:#444}
.news .more{position:absolute;left:297px;top:1019px;font-family:var(--heading);font-size:13px;color:#666;letter-spacing:.5px}
.testimonials h3{left:431px;top:797px}
.dots{position:absolute;left:729px;top:826px;display:flex;gap:4px}
.dots i{width:5px;height:5px;border-radius:50%;background:#ddd}
.dots i:last-child{background:#666}
.quote{position:absolute;left:424px;top:845px;width:334px;height:165px;background:#fff;border:1px solid #ddd;border-radius:2px;padding:20px 30px 0 33px;font-family:var(--heading);font-size:13px;line-height:23px;color:#333}
.quote .mark{position:absolute;right:18px;bottom:12px;font-size:30px;font-family:Georgia,serif;color:#333}
.quote::after{content:"";position:absolute;right:22px;bottom:-8px;width:14px;height:14px;background:#fff;border-right:1px solid #ddd;border-bottom:1px solid #ddd;transform:rotate(45deg)}
.cite{position:absolute;left:602px;top:1026px;font-family:var(--heading);font-size:13px}
.cite b{font-weight:600}
.cite span{color:var(--accent)}
.tweets h3{left:801px;top:771px}
.tweet-list{position:absolute;left:800px;top:817px;width:274px;background:#fff;border:1px solid #ddd}
.tweet{padding:18px 18px 16px;font-family:var(--heading);font-size:13px;line-height:20px;color:#333}
.tweet+.tweet{border-top:1px solid #ddd}
.tweet .handle{color:#777}
.tweet time{display:block;font-size:11.5px;color:#777;margin-top:8px}
.footer{position:absolute;left:0;top:1092px;width:1200px;height:96px;background:var(--footer)}
.footer-social{position:absolute;left:108px;top:30px;display:flex;gap:11px}
.footer-social span{width:41px;height:41px;border-radius:50%}
.partner-name{position:absolute;top:30px;font-family:var(--heading);font-weight:600;font-size:26px;color:#bbb}
.partner-badge{position:absolute;left:1022px;top:24px;width:74px;height:62px;background:#555;border-radius:3px}
.baseline{position:absolute;left:0;top:1188px;width:1200px;height:29px;background:var(--footer-base);color:#ccc;font-size:12.5px;text-align:center;line-height:27px}
</style>
</head>
<body>
<div class="frame">
  <div class="topline"></div>
  <div class="sheet"></div>

  <header>
    <div class="brand"><span class="brand-dot"></span><div class="brand-name">MTM<small>Meridian Tank Metering</small></div></div>
    <nav class="social" aria-label="Social links">
      <span aria-label="quillane"></span><span aria-label="chirpa"></span><span aria-label="vidora"></span><span aria-label="tubeline"></span><span aria-label="plusring"></span>
    </nav>
  </header>

  <svg class="wave" width="1200" height="460" viewBox="0 0 1200 460" aria-hidden="true">
    <path d="M0 85 C250 20 550 -5 800 10 C1000 22 1150 50 1200 100 L1200 460 L0 460 Z" fill="var(--blue)"/>
    <rect x="102" y="20" width="996" height="440" fill="var(--blue)"/>
    <rect x="116" y="44" width="970" height="406" fill="#fff"/>
  </svg>
  <div class="hero-photo" role="img" aria-label="Photo of two field technicians in high-visibility workwear on a tank roof above a harbour"></div>
  <aside class="services">
    <h2>Our Expert <em>Technical</em></h2>
    <ul>
      <li>Planned Maintenance</li>
      <li>System calibrations, validations</li>
      <li>System monitoring and repair</li>
      <li>Emergency Breakdowns</li>
      <li>Remote support</li>
      <li>Customer training</li>
      <li>WirelessPULSE systems</li>
      <li>System commissioning</li>
      <li>Technical and Operational Training</li>
      <li>Service &amp; Maintenance</li>
    </ul>
  </aside>

  <section class="about">
    <h3>Meridian Tank Metering</h3>
    <div class="can" role="img" aria-label="Illustration of a silver storage tank"></div>
    <p>Lorem ipsum dolor sit amet, consectetur adipiscing elit. Quisque dapibus accumsan orci, pretium eleifend arcu adipiscing eget. Fusce accumsan facilisis tincidunt. Phasellus tempor enim purus, vitae venenatis est. Ut imperdiet hendrerit pulvinar. Cras at tellus a enim condimentum mollis ut et tellus. Mauris dolor magna, elementum eu dictum eu, fermentum a nibh. Praesent ut dui lectus, vel lacinia sem. Praesent commodo malesuada urna, quis convallis risus dictum et.</p>
  </section>
  <div class="divider"></div>
  <section class="support">
    <h3>Project Support</h3>
    <p>We work closely with you to understand your exact metering, gauging and associated controls and mass balancing requirements to assist implement-ing the best solution for your project. Our expert services include:-</p>
  </section>

  <section class="news">
    <h3>Latest News</h3>
    <h4>Lorem ipsum dolor sit amet</h4>
    <div class="date">14<sup>th</sup> November</div>
    <p>Nam libero tempore, cum soluta nobis est eligendi optio cumque nihil impedit quo lorem ipsum dolor sit &nbsp;minus id quod maxime placeat facere possimus, omnis voluptas assumenda est, omnis dolor repellendus...</p>
    <a class="more">FULL ARTICLE &nbsp;›</a>
  </section>

  <section class="testimonials">
    <h3>Client Testimonials</h3>
    <div class="dots"><i></i><i></i><i></i></div>
    <blockquote class="quote">At vero eos et accusamus et lucero iusto odio dignissimos ducimus qui blanditiis praesentium voluptatum deleniti atque corrupti quos dolores et quas molestias excepturi sint occaecati cupiditate non provident.<span class="mark">”</span></blockquote>
    <div class="cite"><b>John Doe</b>, <span>xyz etc.</span>, cat lover</div>
  </section>

  <section class="tweets">
    <h3>Recent Tweets</h3>
    <div class="tweet-list">
      <div class="tweet"><span class="handle">@ironmarsh</span> Lorem ipsum dolor sit amet consectetur adipisicing elit.<time>9 hours ago</time></div>
      <div class="tweet"><span class="handle">@bluesedge</span> At vero eos et accusamus et iusto odio dignissimos ducimus blanditiis praesentium voluptatum<time>1 day ago</time></div>
    </div>
  </section>

  <footer class="footer">
    <div class="footer-social">
      <span style="background:#1c4f7e" aria-label="quillane"></span>
      <span style="background:#1aa3dd" aria-label="chirpa"></span>
      <span style="background:#f0901e" aria-label="feed"></span>
      <span style="background:#bdbdbd" aria-label="email"></span>
    </div>
    <div class="partner-name" style="left:592px">MTM</div>
    <div class="partner-name" style="left:750px;color:#fff">PULSE</div>
    <div class="partner-badge" aria-hidden="true"></div>
  </footer>
  <div class="baseline">Copyright © 2014 Meridian Tank Metering Solutions | Disclaimer</div>
</div>
</body>
</html>
```